High-end Oceanfront Real Estate Group Needs Clean, Modern Web Design

I’m looking for a clean, professional, modern and beautiful homepage web design for a Real Estate group in Southern California, USA.

The group/company is “Marlow on the Shore,” and they specialize in high end (i.e. expensive), oceanfront real estate in the Orange County area.

The look and feel of the page should accentuate the brand qualities: luxurious/expensive, professional, and beautiful (Orange County is one of the most beautiful areas in all the US and we would love the site to emphasize the beautiful beaches and scenery it has to offer).

Looks we like:
• www.brantleyhomesrealty.example
• www.keptbyfenwick.example -- I think the design is pretty out-dated in this site, but I like the organization/layout of the site

Header Tags (I don’t know if we can fit all of these, may need a side-menu, but I’d prefer header title only if possible):
• Welcome
• Featured Listings
• Previously Sold
• Sell
• Property Search
• Team
• Videos
• Blog
• Explore O.C.
• Contact

I have attached the beach and logo pics that we would like to use as the header, a few pictures of the team, and one sample home/view pic which can be used in any of the other sections (for pictures of the homes, just find expensive oceanfront houses and that will be fine).

I promise to provide feedback to each and every design submission. I appreciate the hard work that all of you are putting into your designs. There can be only one contest winner, but I hope to give all of you helpful feedback to submit the best designs possible!

Target Market(s)

Very wealthy home owners of oceanfront properties. These properties are worth several millions of dollars, and thus the site and brand needs to be targeted to very wealthy, successful individuals and families (both US and international buyers).

Industry/Entity Type

Real Estate

Number of Pages Required

2 page

Requirements
Must have
• I don’t want to give too many requirements, because I want to let you all be creative. However, here are the few Must Haves:
• Must submit 2 page designs (a home page and a sub page)
• Must use logo provided
• Focus is mostly on homes, but I would like to include some beach/ocean imagery as well
• The first “item” on the home page should be an accordion/slider which shows pictures of homes and with 1 line of text: “List with the Leader” and two link buttons: “Sell Your Home” and “Buy Your Home”
• Color palette needs to be mainly blues--to match ocean and sky blue
• Exported in all major formats (psd,ai,eps,png,jpeg,etc)
Nice to have
• We don’t necessarily need all of these, but would like to feature most:
• List of videos
• “Meet the Team”—brief team bios and pics
• Link(s) to Blog
• “List with the Leader” – section on why they should choose this firm
• Featured Listings
• Previously Sold

```html
<!DOCTYPE html>
<html lang="en">
<head>
<meta charset="utf-8">
<title>Marlow on the Shore — Oceanfront Real Estate</title>
<link href="https://fonts.googleapis.com/css2?family=Raleway:wght@300;400;500;600&family=Open+Sans:wght@400;600&family=Playfair+Display:wght@700&display=swap" rel="stylesheet">
<style>
:root{
  --teal:#2fb8c9;
  --teal-dark:#239fae;
  --ink:#333;
  --muted:#8a8a8a;
  --line:#e2e2e2;
  --band:#f4f4f4;
  --footer:#262626;
  --footer-text:#9a9a9a;
  --white:#fff;
}
*{margin:0;padding:0;box-sizing:border-box}
html,body{width:1200px;height:2528px;overflow:hidden;background:var(--white)}
body{position:relative;font-family:"Open Sans",Arial,sans-serif;color:var(--ink)}
.abs{position:absolute}
.heading{font-family:"Raleway",Arial,sans-serif;font-weight:400;font-size:24px;color:#444;letter-spacing:.5px;text-transform:uppercase}
.intro{font-size:13px;line-height:22px;color:var(--muted);text-align:center}

/* hero */
.hero{left:0;top:0;width:1200px;height:696px;background:linear-gradient(180deg,#3a6fae 0%,#7ba3cc 34%,#5f7f8e 46%,#3d5a3a 62%,#2f4a26 100%)}
.sidenav{left:100px;top:0;width:217px;height:660px}
.sidenav svg{position:absolute;left:0;top:0}
.brand{position:absolute;left:18px;top:44px;width:185px;height:60px}
.brand-mark{position:absolute;left:0;top:8px;width:12px;height:12px;background:var(--teal)}
.brand-name{position:absolute;left:22px;top:0;width:160px;font-family:"Open Sans",Arial,sans-serif;font-weight:600;font-size:19px;line-height:27px;color:var(--ink)}
.menu{position:absolute;left:0;top:145px;width:217px;list-style:none}
.menu li{height:41px;line-height:41px;padding-left:20px;font-size:12.5px;color:#333;text-transform:uppercase;border-bottom:1px solid rgba(255,255,255,.55)}
.menu li.active{background:var(--teal);color:var(--white)}
.hero-title{left:400px;top:160px;width:656px;text-align:center;font-family:"Raleway",Arial,sans-serif;font-weight:300;font-size:46px;letter-spacing:2px;color:var(--white)}
.btn{top:248px;height:40px;line-height:38px;text-align:center;font-family:"Raleway",Arial,sans-serif;font-weight:600;font-size:15px;color:var(--white);text-transform:uppercase}
.btn-sell{left:521px;width:182px;background:var(--teal);border:1px solid var(--teal)}
.btn-buy{left:718px;width:180px;border:2px solid var(--white)}
.slider-arrows{left:1048px;top:657px;width:44px;height:23px;background:rgba(0,0,0,.35)}

/* featured */
.card{top:841px;width:241px;height:317px;border:1px solid var(--line);box-shadow:0 1px 3px rgba(0,0,0,.08);background:var(--white)}
.card .photo{position:absolute;left:5px;top:5px;width:229px;height:197px}
.price{position:absolute;right:30px;top:5px;height:30px;line-height:30px;padding:0 8px;background:var(--teal);color:var(--white);font-size:15px;font-weight:600}
.tag{position:absolute;right:5px;top:5px;width:25px;height:30px;background:#3a3a3a}
.card h3{position:absolute;top:228px;width:100%;text-align:center;font-family:"Raleway",Arial,sans-serif;font-weight:600;font-size:13px;color:#222;text-transform:uppercase}
.card p{position:absolute;top:256px;left:10px;right:10px;text-align:center;font-size:11px;line-height:19px;color:var(--muted)}

/* videos & blog */
.video-main{left:100px;top:1243px;width:675px;height:233px;background:linear-gradient(180deg,#5d7aa0 0%,#b59a6e 45%,#6e5a3e 70%,#4a4a44 100%)}
.thumb{top:1484px;width:86px;height:68px}
.thumb.current{outline:3px solid #d9d9d9;outline-offset:-3px}
.post{left:794px;width:308px;height:108px;border-bottom:1px solid var(--line)}
.post .day{position:absolute;left:0;top:-2px;font-family:"Playfair Display",serif;font-size:36px;color:var(--teal);line-height:40px}
.post .month{position:absolute;left:2px;top:38px;font-family:"Playfair Display",serif;font-size:15px;color:#222}
.post h4{position:absolute;left:58px;top:0;font-size:12.5px;font-weight:400;color:#222;white-space:nowrap}
.post p{position:absolute;left:58px;top:24px;width:250px;font-size:11px;line-height:19px;color:var(--muted)}

/* team */
.team-band{left:0;top:1600px;width:1200px;height:355px;background:var(--band);border-top:1px solid var(--line);border-bottom:1px solid var(--line)}
.member{top:1735px;width:231px;height:181px;overflow:hidden}
.member .caption{position:absolute;left:0;bottom:0;width:100%;height:52px;background:rgba(0,0,0,.55);text-align:center}
.member .name{display:block;margin-top:3px;font-family:"Raleway",Arial,sans-serif;font-size:18px;color:var(--teal)}
.member .role{display:block;font-size:11px;color:var(--white)}

/* previously sold */
.sold{left:100px;width:605px;height:110px}
.sold .photo{position:absolute;left:0;top:0;width:148px;height:105px;border:3px solid var(--white);box-shadow:0 0 0 1px var(--line)}
.sold h4{position:absolute;left:162px;top:0;font-family:"Raleway",Arial,sans-serif;font-weight:500;font-size:15px;color:#222}
.sold p{position:absolute;left:162px;top:28px;width:443px;font-size:10.5px;line-height:19.5px;color:#555}
.acc{left:735px;width:367px;background:#f1f1f1;border:1px solid var(--line)}
.acc .row{height:41px;line-height:41px;padding-left:38px;font-family:"Raleway",Arial,sans-serif;font-size:16px;color:#333;position:relative}
.acc .row svg{position:absolute;left:10px;top:13px}
.acc.open .row{color:var(--teal)}
.acc .body{background:var(--white);padding:10px 12px;font-size:10.5px;line-height:19px;color:#666;border-top:1px solid var(--line)}
.acc .body a{color:var(--teal);text-decoration:none}
.pager{left:1071px;top:1996px;width:31px;height:16px;background:#bbb}

/* footer */
.footer{left:0;top:2345px;width:1200px;height:183px;background:var(--footer)}
.footer h5{position:absolute;top:18px;font-family:"Raleway",Arial,sans-serif;font-weight:400;font-size:16px;color:#e6e6e6}
.contact{position:absolute;top:60px;font-size:11px;line-height:19px;color:var(--footer-text)}
.contact svg{position:absolute;left:0;top:0}
.contact span{position:absolute;left:46px;top:3px;white-space:nowrap}
.social{position:absolute;top:61px;width:24px;height:24px;border-radius:50%;background:#4a4a4a}
.copyright{position:absolute;top:141px;width:100%;text-align:center;font-size:11px;color:#8a8a8a}
.rule{position:absolute;left:0;top:125px;width:100%;height:1px;background:#333}
</style>
</head>
<body>

<!-- hero -->
<section class="abs hero" role="img" aria-label="Oceanfront resort estate with palm trees, lawns and a gazebo under a blue sky"></section>

<nav class="abs sidenav">
  <svg width="217" height="660" viewBox="0 0 217 660">
    <polygon points="0,0 217,0 217,556 108,660 0,556" fill="rgba(255,255,255,.78)"/>
  </svg>
  <div class="brand">
    <span class="brand-mark"></span>
    <span class="brand-name">Marlow on the Shore</span>
  </div>
  <ul class="menu">
    <li class="active">• Welcome</li>
    <li>• Featured Listings</li>
    <li>• Previously Sold</li>
    <li>• Sell</li>
    <li>• Property Search</li>
    <li>• Team</li>
    <li>• Videos</li>
    <li>• Blog</li>
    <li>• Explore O.C</li>
    <li>• Contact</li>
  </ul>
</nav>

<h1 class="abs hero-title">LIST WITH THE LEADER</h1>
<a class="abs btn btn-sell">Sell Your Home</a>
<a class="abs btn btn-buy">Buy Your Home</a>
<div class="abs slider-arrows">
  <svg width="44" height="23" viewBox="0 0 44 23"><path d="M15 7l-4 4.5 4 4.5M29 7l4 4.5-4 4.5" stroke="#fff" stroke-width="1.5" fill="none"/><line x1="22" y1="4" x2="22" y2="19" stroke="rgba(255,255,255,.4)"/></svg>
</div>

<!-- featured listings -->
<h2 class="abs heading" style="left:0;top:728px;width:1200px;text-align:center">Featured Listings</h2>
<p class="abs intro" style="left:200px;top:768px;width:800px">lorem ipsum dolor sit amet, consectetur adipiscing elit. Ut volutpat rutrum eros sit amet sollicitudin. Suspendisse pulvinar, velit nec pharetar, velit nec pharet ra interdumante.</p>

<article class="abs card" style="left:100px">
  <div class="photo" role="img" aria-label="Aerial view of a luxury estate with winding drive and green lawns" style="background:linear-gradient(160deg,#6f8f4a,#3f6a2e 60%,#8a7a5a)"></div>
  <span class="price">$5000,00</span><span class="tag"><svg width="25" height="30" viewBox="0 0 25 30"><path d="M7 10h6l6 6-5 5-7-7z" fill="#fff"/><circle cx="10" cy="13" r="1.2" fill="#3a3a3a"/></svg></span>
  <h3>Beautiful Luxury Homes Sold</h3>
  <p>Dolor nunc vule putateulr ips dol consem donec comete dolo lectus fgilla.</p>
</article>
<article class="abs card" style="left:354px">
  <div class="photo" role="img" aria-label="Poolside patio with blossoming bougainvillea and stone fireplace" style="background:linear-gradient(180deg,#7aa0c8,#a65a7a 40%,#3fb6d6 75%,#d9d4c8)"></div>
  <span class="price">$5000,00</span><span class="tag"><svg width="25" height="30" viewBox="0 0 25 30"><path d="M7 10h6l6 6-5 5-7-7z" fill="#fff"/><circle cx="10" cy="13" r="1.2" fill="#3a3a3a"/></svg></span>
  <h3>Beautiful Luxury Homes Sold</h3>
  <p>Dolor nunc vule putateulr ips dol consem donec comete dolo lectus fgilla.</p>
</article>
<article class="abs card" style="left:608px">
  <div class="photo" role="img" aria-label="Warm living room with wooden beamed ceiling and fireplace" style="background:linear-gradient(180deg,#6e4326,#b07a4a 50%,#8a5232)"></div>
  <span class="price">$5000,00</span><span class="tag"><svg width="25" height="30" viewBox="0 0 25 30"><path d="M7 10h6l6 6-5 5-7-7z" fill="#fff"/><circle cx="10" cy="13" r="1.2" fill="#3a3a3a"/></svg></span>
  <h3>Beautiful Luxury Homes Sold</h3>
  <p>Dolor nunc vule putateulr ips dol consem donec comete dolo lectus fgilla.</p>
</article>
<article class="abs card" style="left:861px">
  <div class="photo" role="img" aria-label="Marble bathroom with glass shower and tall windows" style="background:linear-gradient(180deg,#8a7a66,#c7bca8 50%,#6e6255)"></div>
  <span class="price">$5000,00</span><span class="tag"><svg width="25" height="30" viewBox="0 0 25 30"><path d="M7 10h6l6 6-5 5-7-7z" fill="#fff"/><circle cx="10" cy="13" r="1.2" fill="#3a3a3a"/></svg></span>
  <h3>Beautiful Luxury Homes Sold</h3>
  <p>Dolor nunc vule putateulr ips dol consem donec comete dolo lectus fgilla.</p>
</article>

<!-- videos -->
<h2 class="abs heading" style="left:100px;top:1190px">List of Videos</h2>
<div class="abs video-main" role="img" aria-label="Video still of a Mediterranean villa with garage and wisteria-covered facade">
  <svg style="position:absolute;left:302px;top:81px" width="72" height="72" viewBox="0 0 72 72"><circle cx="36" cy="36" r="33" fill="rgba(255,255,255,.15)" stroke="#fff" stroke-width="3"/><path d="M29 23l20 13-20 13z" fill="#fff"/></svg>
</div>
<div class="abs thumb" style="left:100px;background:linear-gradient(180deg,#5d93c9,#3a78b0 55%,#c8c0a8)" role="img" aria-label="Ocean view"></div>
<div class="abs thumb" style="left:198px;background:linear-gradient(180deg,#6e3a26,#a8704a)" role="img" aria-label="Dining room"></div>
<div class="abs thumb" style="left:296px;background:linear-gradient(180deg,#5a3a2e,#b89a80)" role="img" aria-label="Living room"></div>
<div class="abs thumb current" style="left:394px;background:linear-gradient(180deg,#6a86a8,#b08a5a 55%,#4a4638)" role="img" aria-label="Villa exterior"></div>
<div class="abs thumb" style="left:492px;background:linear-gradient(180deg,#8a5a3a,#c88a5a)" role="img" aria-label="Lounge interior"></div>
<div class="abs thumb" style="left:590px;background:linear-gradient(180deg,#4a6a3a,#2f8aa8 60%,#6a6a5a)" role="img" aria-label="Terrace pool"></div>
<div class="abs thumb" style="left:688px;width:87px;background:linear-gradient(180deg,#8ab0d0,#3ab6d0 60%,#9a8a70)" role="img" aria-label="Spa pool"></div>

<!-- blog -->
<h2 class="abs heading" style="left:794px;top:1190px">Our Blog</h2>
<article class="abs post" style="top:1247px">
  <span class="day">27</span><span class="month">DEC</span>
  <h4>Conse ctetu itaesaert veciegast nveriti vase</h4>
  <p>We can send you email reports of how many people are viewing your listing!  We can even show you how for properties in your price range.</p>
</article>
<article class="abs post" style="top:1358px">
  <span class="day">27</span><span class="month">DEC</span>
  <h4>Conse ctetu itaesaert veciegast nveriti vase</h4>
  <p>We can send you email reports of how many people are viewing your listing!  We can even show you how for properties in your price range.</p>
</article>
<article class="abs post" style="top:1473px;border-bottom:none">
  <span class="day">27</span><span class="month">DEC</span>
  <h4>Conse ctetu itaesaert veciegast nveriti vase</h4>
  <p>We can send you email reports of how many people are viewing your listing!  We can even show you how for properties in your price range.</p>
</article>

<!-- team -->
<section class="abs team-band"></section>
<h2 class="abs heading" style="left:0;top:1624px;width:1200px;text-align:center">Our Teams</h2>
<p class="abs intro" style="left:200px;top:1662px;width:800px">lorem ipsum dolor sit amet, consectetur adipiscing elit. Ut volutpat rutrum eros sit amet sollicitudin. Suspendisse pulvinar, velit nec pharetar, velit nec pharet ra interdumante.</p>

<div class="abs member" style="left:100px;background:linear-gradient(180deg,#a9c3dc,#c9a27a)" role="img" aria-label="Portrait of a team member">
  <div class="caption"><span class="name">John Doe</span><span class="role">Graphic Designer</span></div>
</div>
<div class="abs member" style="left:356px;background:linear-gradient(180deg,#3a2a22,#6a5a50)" role="img" aria-label="Portrait of a team member">
  <div class="caption"><span class="name">John Doe</span><span class="role">Graphic Designer</span></div>
</div>
<div class="abs member" style="left:613px;background:linear-gradient(180deg,#4a4a4a,#8a6a5a)" role="img" aria-label="Portrait of a team member">
  <div class="caption"><span class="name">John Doe</span><span class="role">Graphic Designer</span></div>
</div>
<div class="abs member" style="left:869px;background:linear-gradient(180deg,#d6d2c8,#2a2a30)" role="img" aria-label="Portrait of a team member">
  <div class="caption"><span class="name">John Doe</span><span class="role">Graphic Designer</span></div>
</div>

<!-- previously sold -->
<h2 class="abs heading" style="left:100px;top:1991px">Previously Sold</h2>
<article class="abs sold" style="top:2047px">
  <div class="photo" role="img" aria-label="Arched entry courtyard of a Spanish-style home" style="background:linear-gradient(180deg,#6a86a0,#b07a4a 55%,#4a5a3a)"></div>
  <h4>18 Harbor Crest Lane, Seabluff</h4>
  <p>Lorem ipsum dolor sit amet, ne sea nobis vivendo, brute altera expetendis vis id, in vis assentior efficiendi voluptatibus. Ut sed vidisse virtute perpetua, alia moderatius et qui, quo an.Lorem ipsum dolor sit amet, ne sea nobis vivendo, brute altera expetendis vis id, in vis assentior Ut sed vidisse virtute perpetua, alia moderatius et qui, quo an.</p>
</article>
<div class="abs" style="left:100px;top:2177px;width:605px;height:1px;background:var(--line)"></div>
<article class="abs sold" style="top:2195px">
  <div class="photo" role="img" aria-label="Hillside villa with terraced gardens" style="background:linear-gradient(180deg,#7aa6d0,#d8c8a0 55%,#5a7a3a)"></div>
  <h4>18 Harbor Crest Lane, Seabluff</h4>
  <p>Lorem ipsum dolor sit amet, ne sea nobis vivendo, brute altera expetendis vis id, in vis assentior efficiendi voluptatibus. Ut sed vidisse virtute perpetua, alia moderatius et qui, quo an.Lorem ipsum dolor sit amet, ne sea nobis vivendo, brute altera expetendis vis id, in vis assentior Ut sed vidisse virtute perpetua, alia moderatius et qui, quo an.</p>
</article>

<!-- list with the leader -->
<h2 class="abs heading" style="left:735px;top:1991px">List with the Leader</h2>
<div class="abs pager"><svg width="31" height="16" viewBox="0 0 31 16"><path d="M10 4l-4 4 4 4M21 4l4 4-4 4" stroke="#fff" stroke-width="1.4" fill="none"/></svg></div>

<div class="abs acc open" style="top:2037px">
  <div class="row"><svg width="16" height="16" viewBox="0 0 16 16"><circle cx="8" cy="8" r="8" fill="var(--teal)"/><rect x="4" y="7" width="8" height="2" fill="#fff"/></svg>Neque porro quisquam est qui</div>
  <div class="body">It is a long established fact that a reader will be distracted by the readable content of a page when looking at its layout.The point of using Lorem Ipsum is that it has a more-or-less... <a>[Read More]</a></div>
</div>
<div class="abs acc" style="top:2169px"><div class="row"><svg width="16" height="16" viewBox="0 0 16 16"><circle cx="8" cy="8" r="8" fill="#888"/><rect x="4" y="7" width="8" height="2" fill="#fff"/><rect x="7" y="4" width="2" height="8" fill="#fff"/></svg>Neque porro quisquam est qui</div></div>
<div class="abs acc" style="top:2212px"><div class="row"><svg width="16" height="16" viewBox="0 0 16 16"><circle cx="8" cy="8" r="8" fill="#888"/><rect x="4" y="7" width="8" height="2" fill="#fff"/><rect x="7" y="4" width="2" height="8" fill="#fff"/></svg>Neque porro quisquam est qui</div></div>
<div class="abs acc" style="top:2255px"><div class="row"><svg width="16" height="16" viewBox="0 0 16 16"><circle cx="8" cy="8" r="8" fill="#888"/><rect x="4" y="7" width="8" height="2" fill="#fff"/><rect x="7" y="4" width="2" height="8" fill="#fff"/></svg>Neque porro quisquam est qui</div></div>

<!-- footer -->
<footer class="abs footer">
  <h5 style="left:118px">Contact us</h5>
  <h5 style="left:929px">Follow us on</h5>

  <div class="contact" style="left:112px;width:300px">
    <svg width="30" height="30" viewBox="0 0 30 30"><circle cx="15" cy="15" r="14" fill="none" stroke="#555"/><path d="M15 8a4.5 4.5 0 0 0-4.5 4.5c0 3.5 4.5 9 4.5 9s4.5-5.5 4.5-9A4.5 4.5 0 0 0 15 8z" fill="#888"/><circle cx="15" cy="12.5" r="1.6" fill="#262626"/></svg>
    <span>Address : 4180 Tidewater Drive<br>Coral Cove, CA 92600</span>
  </div>
  <div class="contact" style="left:430px;width:200px">
    <svg width="30" height="30" viewBox="0 0 30 30"><circle cx="15" cy="15" r="14" fill="none" stroke="#555"/><path d="M11 9l3 3-1.5 1.8a8 8 0 0 0 3.7 3.7L18 16l3 3-2 2c-4.5 0-10-5.5-10-10z" fill="#888"/></svg>
    <span>Phone : 555-014-2290</span>
  </div>
  <div class="contact" style="left:648px;width:250px">
    <svg width="30" height="30" viewBox="0 0 30 30"><circle cx="15" cy="15" r="14" fill="none" stroke="#555"/><rect x="9" y="10.5" width="12" height="9" fill="none" stroke="#888" stroke-width="1.4"/><path d="M9 11l6 5 6-5" fill="none" stroke="#888" stroke-width="1.4"/></svg>
    <span>Email : hello@marlowshore.example</span>
  </div>

  <span class="social" style="left:922px"></span>
  <span class="social" style="left:955px;background:#8a8a8a"></span>
  <span class="social" style="left:988px"></span>
  <span class="social" style="left:1021px"></span>
  <span class="social" style="left:1054px"></span>

  <div class="rule"></div>
  <p class="copyright">© Copyright2015 Marlow on the Shore. All rights reserved.</p>
</footer>

</body>
</html>
```